Morden, Creative, Unique, Independent Wine Shop

1. We are a brand new wine shop located in Melbourne Australia, we have our logo already, simply use the logo to design a business card.
2. I have uploaded our logo in two versions, with or without shadow, any of them is acceptable.
3. Make it as creative and unique as possible, no limitation of shape, color combination, geometry pattern, fonts, composing etc.
3. Info on the card:
- Brambleford Wine Cellar (Not very necessary if logo is obviously shown)
- 42 Ferncastle Steet, Hampton, Victoria, Australia 3188
- +61 3 9018 4637
- www.bramblefordwinecellar.com.au
- bramblefordwinecellar@mailvista.com
- Additional icons: Google, Instagram, Facebook, Twitter
4. Once again, forget it is a commercial card, make it special.

```html
<!DOCTYPE html>
<html lang="en">
<head>
<meta charset="utf-8">
<title>Brambleford Wine Cellar – Business Card</title>
<link rel="stylesheet" href="https://fonts.googleapis.com/css2?family=Arimo:wght@400;700&display=swap">
<style>
  :root {
    --bg: #2a2a2c;
    --card: #f7f7f6;
    --wine: #a3123c;
    --grey: #6b6b6b;
    --ink: #3a3a3a;
    --rule: #bdbdbd;
  }
  * { margin: 0; padding: 0; box-sizing: border-box; }
  html, body { width: 1200px; height: 960px; overflow: hidden; }
  body {
    background: var(--bg);
    font-family: "Arimo", Arial, sans-serif;
    position: relative;
  }
  .card {
    position: absolute;
    width: 620px;
    height: 354px;
    background: var(--card);
    border-radius: 3px;
    box-shadow: 0 10px 30px rgba(0,0,0,.45);
  }
  .card-front { left: 500px; top: 70px; }
  .card-back  { left: 80px;  top: 520px; }

  .brand {
    position: absolute;
    left: 50%; top: 50%;
    transform: translate(-50%, -50%);
    display: flex;
    align-items: center;
    gap: 18px;
  }
  .brand-mark {
    width: 58px; height: 58px;
    border-radius: 50%;
    background: var(--wine);
  }
  .brand-name {
    color: var(--wine);
    font-weight: 400;
    font-size: 40px;
    letter-spacing: 2px;
    text-transform: uppercase;
    line-height: 1;
  }
  .brand-sub {
    display: block;
    color: var(--wine);
    font-size: 16px;
    letter-spacing: 6px;
    margin-top: 8px;
  }

  .contact { position: absolute; left: 40px; top: 96px; }
  .person-name {
    color: var(--wine);
    font-weight: 700;
    font-size: 24px;
    letter-spacing: .5px;
    text-transform: uppercase;
  }
  .person-role {
    color: var(--grey);
    font-weight: 700;
    font-size: 16px;
    margin: 2px 0 14px;
  }
  .contact-list { list-style: none; }
  .contact-item {
    display: flex;
    align-items: center;
    gap: 8px;
    color: var(--ink);
    font-size: 15px;
    line-height: 21px;
  }
  .contact-item svg { width: 12px; height: 12px; flex: none; fill: var(--wine); }
  .contact-rule {
    position: absolute;
    left: 36px; right: 36px; top: 282px;
    border-top: 1px solid var(--rule);
  }
  .address {
    position: absolute;
    left: 36px; top: 254px;
    display: flex; align-items: center; gap: 8px;
    color: var(--ink); font-size: 15px;
  }
  .address svg { width: 12px; height: 14px; fill: var(--wine); }

  .back-brand {
    position: absolute;
    right: 46px; top: 70px;
    display: flex; flex-direction: column; align-items: center; gap: 12px;
  }
  .back-brand .brand-mark { width: 84px; height: 84px; }
  .back-brand .brand-name { font-size: 15px; letter-spacing: 2px; }
</style>
</head>
<body>

  <section class="card card-front">
    <div class="brand">
      <div class="brand-mark"></div>
      <div class="brand-name">Brambleford<span class="brand-sub">Wine Cellar</span></div>
    </div>
  </section>

  <section class="card card-back">
    <div class="contact">
      <div class="person-name">Daniel Hartwell</div>
      <div class="person-role">President</div>
      <ul class="contact-list">
        <li class="contact-item">
          <svg viewBox="0 0 12 12"><path d="M2.4 0.5l2 2.2-1 1.4c.7 1.6 2 2.9 3.6 3.6l1.4-1 2.2 2-1 2.1C5.8 10.6 1.4 6.2.5 2.4z"/></svg>
          +61 3 9018 4637
        </li>
        <li class="contact-item">
          <svg viewBox="0 0 12 12"><path d="M0 2h12v8H0z M0 2l6 4.5L12 2" stroke="#fff" stroke-width="1"/></svg>
          bramblefordwinecellar@mailvista.com
        </li>
        <li class="contact-item">
          <svg viewBox="0 0 12 12"><circle cx="6" cy="6" r="6"/><path d="M1 6h10M6 0c-2.5 3-2.5 9 0 12M6 0c2.5 3 2.5 9 0 12" stroke="#fff" stroke-width=".9" fill="none"/></svg>
          www.bramblefordwinecellar.com.au
        </li>
      </ul>
    </div>
    <div class="address">
      <svg viewBox="0 0 12 14"><path d="M6 0a5 5 0 0 1 5 5c0 3.5-5 9-5 9S1 8.5 1 5a5 5 0 0 1 5-5zm0 3a2 2 0 1 0 0 4 2 2 0 0 0 0-4z"/></svg>
      42 Ferncastle Steet, Hampton, Victoria, Australia 3188
    </div>
    <div class="contact-rule"></div>
    <div class="back-brand">
      <div class="brand-mark"></div>
      <div class="brand-name">Brambleford</div>
    </div>
  </section>

</body>
</html>
```